Business Card Design for Vintage Jazz

I am a vintage jazz band leader in New York City. My groups play the music of the 1920s, 1930s and 1940s. My website is morvainhale.com for more info on what I do.

I am looking for a two sided business card design that has the look and feel of a really nice business card from the 1930s. I need to convey with the design that my work has that vintage kind of class and style, but also conveys that we are fun and entertaining.

Most importantly it should make a bold staement. If Walt Pemberly had a card, what would it have looked like? I want a card that I feel confident will make an impact and will let people know that my work is te the top that NYC has to offer in vintage jazz..

Note that I have only decided to avoid the "committed payment" option as I have not used this service before. Assuming that I get quality work I will select a design from those presented.

Target Market(s)

people who want to hire my band for events, media, and new fans of the band

Industry/Entity Type

Performing Art

Contact Information for Business Card

Definitely a matte finish, possibly a sort of old style of paper with that brown tint? definitely a thick card.

Requirements
Must have
• FRONT
• My name: Tobias Merrow
• What I do: Bandleader, Guitarist, Vocalist, Songwriter
• Contact Details: morvainhale.com tobias@morvainhale.com 646-555-0184
• BACK
• My Social Media Links:
• facebook.morvainhale.com
• twitter, instagram, linkedin: morvainhale
• I'm also including a photo image I would like to use. The photo's background is not needed, and to be honest isn't really desireable. Just looking to use the image of me.
Nice to have
• I'm attaching which could be used as is, omitted from the card, or altered maybe with text going around the outside of the circle or in some other way. It may need some clean up to the edges of the lettering as we only use it for the website thumbnail.
• If there's space I'd like to include the text "join our mailing list for a free song download: freesong.morvainhale.com" If not perhaps just "Download a Free Song at: freesong.morvainhale.com - something to this end.
Should not have
• anything cartoony. Don't think retro 90s's vision of the swing era, think actual swing era!
• anything modern. Got to look old school
• Try to avoid dark backgrounds. Since we often play in bars and clubs where it is dar, a d
• avoid script fonts.

```html
<!DOCTYPE html>
<html lang="en">
<head>
<meta charset="utf-8">
<title>Tobias Merrow – Business Card</title>
<link href="https://fonts.googleapis.com/css2?family=Open+Sans:wght@400;600;700&display=swap" rel="stylesheet">
<style>
  :root {
    --backdrop: #2a2a2c;
    --paper: #f3eee2;
    --paper-edge: #e4dccb;
    --teal: #4fae97;
    --teal-deep: #3f9480;
    --ink: #3e3a35;
    --ink-soft: #5f5850;
    --photo-dark: #3a3835;
    --photo-light: #a39d94;
  }
  * { margin: 0; padding: 0; box-sizing: border-box; }
  html, body {
    width: 1200px; height: 795px; overflow: hidden;
    background: var(--backdrop);
    font-family: "Open Sans", Arial, sans-serif;
  }
  .canvas { position: relative; width: 1200px; height: 795px; }
  .card {
    position: absolute; width: 560px; height: 320px;
    background: radial-gradient(ellipse at 50% 40%, var(--paper) 55%, var(--paper-edge) 100%);
    border-radius: 22px;
    box-shadow: 0 10px 30px rgba(0,0,0,.45);
  }
  .card::before {
    content: ""; position: absolute; inset: 12px;
    border: 1px solid rgba(79,174,151,.45); border-radius: 14px;
    box-shadow: inset 0 0 0 3px var(--paper), inset 0 0 0 4px rgba(79,174,151,.3);
    pointer-events: none;
  }
  .name {
    color: var(--teal); font-weight: 700; letter-spacing: .5px;
    line-height: 1; white-space: nowrap;
  }

  /* Front */
  .card--front { left: 40px; top: 80px; }
  .portrait {
    position: absolute; left: 40px; top: 50px;
    width: 220px; height: 220px; border-radius: 50%;
    background:
      radial-gradient(ellipse 45% 60% at 52% 72%, var(--photo-dark) 0 60%, transparent 62%),
      radial-gradient(circle at 52% 30%, var(--photo-light) 0 13%, transparent 14%),
      var(--teal);
    box-shadow: 0 3px 8px rgba(0,0,0,.25);
  }
  .front-text {
    position: absolute; left: 272px; top: 104px; width: 268px; text-align: center;
  }
  .front-text .name { font-size: 31px; }
  .front-text .role { font-size: 12px; color: var(--ink-soft); margin-top: 8px; white-space: nowrap; }
  .social {
    display: flex; justify-content: center; align-items: center; gap: 7px; margin-top: 12px;
  }
  .social .dot { width: 15px; height: 15px; border-radius: 50%; background: var(--teal); }
  .social .handle { font-size: 11.5px; color: var(--ink-soft); margin-left: 4px; }
  .front-text .url {
    font-size: 13.5px; color: var(--ink); letter-spacing: 3px; margin-top: 12px; white-space: nowrap;
  }
  .front-text .url b { font-weight: 600; }

  /* Back */
  .card--back { left: 600px; top: 395px; text-align: center; }
  .monogram-disc {
    width: 62px; height: 62px; border-radius: 50%; background: var(--teal);
    margin: 56px auto 12px;
  }
  .card--back .name { font-size: 36px; }
  .card--back .role {
    font-size: 13.5px; color: var(--ink); letter-spacing: 1px; margin-top: 10px; white-space: nowrap;
  }
  .contacts {
    display: flex; justify-content: center; align-items: center; gap: 12px;
    margin-top: 22px; font-size: 13.5px; color: var(--ink); white-space: nowrap;
  }
  .contact { display: flex; align-items: center; gap: 5px; }
  .contact svg { width: 14px; height: 14px; flex: none; }
</style>
</head>
<body>
<main class="canvas">
  <section class="card card--front">
    <div class="portrait" role="img" aria-label="Portrait of the bandleader in a dark piped blazer, tipping a straw boater hat, on a teal circle"></div>
    <div class="front-text">
      <h1 class="name">Tobias Merrow</h1>
      <p class="role">Bandleader, Guitarist, Vocalist, Songwriter</p>
      <div class="social" aria-label="Social media: morvainhale">
        <span class="dot"></span><span class="dot"></span><span class="dot"></span><span class="dot"></span>
        <span class="dot"></span><span class="dot"></span>
        <span class="handle">/morvainhale</span>
      </div>
      <p class="url">www.<b>morvainhale</b>.com</p>
    </div>
  </section>

  <section class="card card--back">
    <div class="monogram-disc"></div>
    <h2 class="name">Tobias Merrow</h2>
    <p class="role">BANDLEADER,&nbsp; GUITARIST,&nbsp; VOCALIST,&nbsp; SONGWRITER</p>
    <div class="contacts">
      <span class="contact">
        <svg viewBox="0 0 14 14" aria-hidden="true"><circle cx="7" cy="7" r="7" fill="var(--teal)"/><path d="M4.5 3.5l1.5 0 .6 1.8-.9.7a5 5 0 0 0 2.3 2.3l.7-.9 1.8.6v1.5c-3.5.3-6.3-2.5-6-6z" fill="#fff"/></svg>
        646-555-0184
      </span>
      <span class="contact">
        <svg viewBox="0 0 14 14" aria-hidden="true"><circle cx="7" cy="7" r="7" fill="var(--teal)"/><rect x="3.5" y="4.5" width="7" height="5" fill="none" stroke="#fff" stroke-width="1"/><path d="M3.5 4.5L7 7.3l3.5-2.8" fill="none" stroke="#fff" stroke-width="1"/></svg>
        tobias@morvainhale.com
      </span>
      <span class="contact">
        <svg viewBox="0 0 14 14" aria-hidden="true"><circle cx="7" cy="7" r="7" fill="var(--teal)"/><circle cx="7" cy="7" r="4" fill="none" stroke="#fff" stroke-width=".9"/><path d="M3 7h8M7 3c-2 2.2-2 5.8 0 8M7 3c2 2.2 2 5.8 0 8" fill="none" stroke="#fff" stroke-width=".9"/></svg>
        www.morvainhale.com
      </span>
    </div>
  </section>
</main>
</body>
</html>
```